CD Design Cover - "Beyond the Orchard Gate"

I need a CD cover design. The original Album or CD was recorded in the early eighties. We are re-mastering it. It needs a fresh cover. The genre' is contemporary Christian music and the title of the album is "Beyond the Orchard Gate." This is referring to caring outside of the church walls. A picture of the solo artist could be integrated in the back design. It is not a good picture and does not have to be used. You would have to be creative in using it because of the quality. It does not have to be used at all. I also added some pictures I liked that could be used. I think I like the "Empty church opening" the best. Fits the theme perfectly.

Target Market(s)

30 years old and older.

Requirements
Must have
• Warmth
Nice to have
• I attached two pictures. One of an empty church and one with a reflection of a stain glass window on the wall. It would be nice to see some offerings using these pictures.
Should not have
• Not too churchy

```html
<!DOCTYPE html>
<html lang="en">
<head>
<meta charset="utf-8">
<title>Beyond the Orchard Gate – Back Cover</title>
<link rel="stylesheet" href="https://fonts.googleapis.com/css2?family=Cormorant+Upright:wght@400;500&display=swap">
<style>
  :root {
    --ink: #fbf6ee;
    --ink-soft: rgba(251, 246, 238, 0.86);
    --plum-deep: #2a1830;
  }
  html, body {
    margin: 0;
    padding: 0;
    width: 1200px;
    height: 1188px;
    overflow: hidden;
    background: var(--plum-deep);
  }
  .back-cover {
    position: relative;
    width: 1200px;
    height: 1188px;
    overflow: hidden;
    font-family: "Cormorant Upright", serif;
    color: var(--ink);
  }
  .light-wash {
    position: absolute;
    inset: 0;
    background:
      radial-gradient(ellipse 260px 520px at 330px 260px, rgba(236, 205, 120, 0.85), transparent 70%),
      radial-gradient(ellipse 220px 420px at 470px 760px, rgba(214, 170, 95, 0.7), transparent 70%),
      radial-gradient(ellipse 140px 360px at 200px 520px, rgba(200, 225, 240, 0.55), transparent 70%),
      radial-gradient(ellipse 90px 200px at 110px 330px, rgba(60, 180, 210, 0.55), transparent 70%),
      radial-gradient(ellipse 60px 90px at 80px 260px, rgba(230, 60, 110, 0.6), transparent 70%),
      radial-gradient(ellipse 520px 420px at 1000px 240px, rgba(70, 40, 85, 0.9), transparent 75%),
      radial-gradient(ellipse 600px 500px at 900px 900px, rgba(170, 120, 100, 0.75), transparent 75%),
      linear-gradient(100deg, #2b1934 0%, #4b34a0 10%, #6f5cc0 17%, #c9b070 30%, #b88a48 45%, #7d5a55 62%, #4a2d4f 80%, #3b2440 100%);
  }
  .track-list {
    position: absolute;
    left: 773px;
    top: 92px;
    margin: 0;
    padding: 0;
    list-style: none;
  }
  .track-list li {
    font-size: 35px;
    font-weight: 500;
    line-height: 56px;
    white-space: nowrap;
  }
  .credits,
  .label-block {
    position: absolute;
    left: 787px;
    font-size: 20px;
    font-weight: 500;
    line-height: 24.5px;
    color: var(--ink-soft);
    white-space: nowrap;
  }
  .credits { top: 942px; }
  .label-block { top: 1066px; }
  .credits p,
  .label-block p { margin: 0; }
</style>
</head>
<body>
  <main class="back-cover">
    <div class="light-wash" role="img" aria-label="Photograph of stained glass window light falling as soft coloured bands across a warm plaster wall"></div>

    <ol class="track-list">
      <li>Morning Errand</li>
      <li>Beyond the Orchard Gate</li>
      <li>Common Ground</li>
      <li>The Night the River Sang</li>
      <li>Still Here</li>
      <li>One More Lamp Tonight</li>
      <li>A Quiet Table</li>
      <li>Down the Long Road</li>
      <li>Kinder Than Morning</li>
      <li>Open Hands, Open Door</li>
    </ol>

    <div class="credits">
      <p>Producer:&nbsp; Marla Hensley</p>
      <p>Engineered:&nbsp; Peter Kowalczyk</p>
      <p>Recorded at: Cedar Hollow Studio</p>
      <p>Promoter:&nbsp; Ray Tolliver</p>
    </div>

    <div class="label-block">
      <p>CEDAR HOLLOW</p>
      <p>Fairhaven, MO&nbsp; 65010</p>
    </div>
  </main>
</body>
</html>
```